BRL Design Business Card

I need to develop a business card for my real estate design and investment company. Something clean, classic and professional with a modern vibe.

Industry/Entity Type

Real Estate

Font styles to use
Serif
Sans Serif

```html
<!DOCTYPE html>
<html lang="en">
<head>
<meta charset="utf-8">
<title>BRL Design Business Card</title>
<link rel="stylesheet" href="https://fonts.googleapis.com/css2?family=Questrial&family=Playfair+Display:ital,wght@1,700&family=Libre+Baskerville:ital@1&display=swap">
<style>
  :root {
    --page: #ffffff;
    --card-light: #ffffff;
    --card-dark: #3b3939;
    --ink: #1a1a1a;
    --ink-light: #f2f2f2;
    --shadow: rgba(0, 0, 0, 0.28);
  }
  * { box-sizing: border-box; margin: 0; padding: 0; }
  html, body {
    width: 927px;
    height: 1200px;
    overflow: hidden;
    background: var(--page);
  }
  .sheet {
    position: relative;
    width: 927px;
    height: 1200px;
  }
  .card {
    position: absolute;
    top: 108px;
    width: 224px;
    height: 394px;
    box-shadow: 3px 4px 7px var(--shadow);
    overflow: hidden;
  }
  .card--front { left: 232px; background: var(--card-light); }
  .card--back { left: 494px; background: var(--card-dark); }

  /* Front */
  .front__lower {
    position: absolute;
    left: 0; right: 0; bottom: 0;
    height: 147px;
    background: var(--card-dark);
  }
  .brand {
    position: absolute;
    left: 0; right: 0;
    top: 104px;
    text-align: center;
    color: var(--ink);
    font-family: "Questrial", sans-serif;
    white-space: nowrap;
  }
  .brand__name {
    font-size: 50px;
    letter-spacing: 6px;
    line-height: 1;
    padding-left: 6px;
  }
  .brand__tagline {
    margin-top: 6px;
    font-size: 10px;
  }
  .dots {
    position: absolute;
    top: 207px;
    left: 0; right: 0;
    display: flex;
    justify-content: center;
    gap: 8px;
  }
  .dots span {
    width: 11px;
    height: 11px;
    border-radius: 50%;
    background: var(--ink);
  }
  .holder {
    position: absolute;
    top: 223px;
    left: 0; right: 0;
    text-align: center;
    font-family: "Playfair Display", serif;
    font-style: italic;
    font-weight: 700;
    font-size: 17px;
    line-height: 22px;
    color: var(--ink);
  }
  .contact {
    position: absolute;
    left: 0; right: 0;
    text-align: center;
    color: var(--ink-light);
    font-family: "Questrial", sans-serif;
    font-size: 9px;
    letter-spacing: 1px;
    white-space: nowrap;
  }
  .contact--email { top: 268px; }
  .contact--web { top: 291px; }
  .address {
    position: absolute;
    top: 324px;
    left: 0; right: 0;
    text-align: center;
    color: var(--ink-light);
    font-family: "Libre Baskerville", serif;
    font-style: italic;
    font-size: 8.5px;
    line-height: 14px;
  }
  .phones {
    position: absolute;
    bottom: 16px;
    left: 14px; right: 14px;
    display: flex;
    justify-content: space-between;
    color: var(--ink-light);
    font-family: "Questrial", sans-serif;
    font-size: 8px;
    letter-spacing: 0.6px;
    white-space: nowrap;
  }

  /* Back */
  .back__tagline,
  .back__name {
    position: absolute;
    top: 62px;
    height: 263px;
    writing-mode: vertical-rl;
    transform: rotate(180deg);
    white-space: nowrap;
    text-align: center;
    color: var(--ink-light);
    font-family: "Questrial", sans-serif;
    line-height: 1;
  }
  .back__tagline {
    left: 31px;
    width: 22px;
    font-size: 21px;
  }
  .back__name {
    left: 62px;
    width: 130px;
    font-size: 130px;
    letter-spacing: 8px;
  }
</style>
</head>
<body>
  <main class="sheet">
    <section class="card card--front" aria-label="Business card front">
      <div class="brand">
        <div class="brand__name">BRL</div>
        <div class="brand__tagline">Design and Development</div>
      </div>
      <div class="front__lower"></div>
      <div class="dots" aria-hidden="true">
        <span></span><span></span><span></span><span></span><span></span>
        <span></span><span></span><span></span><span></span><span></span>
      </div>
      <p class="holder">Alex Morgan</p>
      <p class="contact contact--email">Email. alexmorgan@brldesign.com</p>
      <p class="contact contact--web">www.brldesign.com</p>
      <p class="address">456 W. Maple Avenue<br>Springdale, State, 54321</p>
      <div class="phones">
        <span>Tel. 987 654 321</span>
        <span>Fax. 987 654 320</span>
      </div>
    </section>

    <section class="card card--back" aria-label="Business card back">
      <span class="back__tagline">Design and Development</span>
      <span class="back__name">BRL</span>
    </section>
  </main>
</body>
</html>
```